MOLVT Study flyer

I need help designing a flyer for a research study that will include brain imaging in adolescents. The info is in the attached document. The study is called the Marrowby Orchard Lantern Vesper Trail (MOLVT) study. Ideally this would be returned as a document that I can edit in the future as we will have several new recruitment phases (different age groups, etc. I also would love to have a logo designed as part of this project, but I recognize that might be a separate design request.

```html
<!DOCTYPE html>
<html lang="en">
<head>
<meta charset="utf-8">
<title>MOLVT Study – Recruitment Flyer</title>
<link href="https://fonts.googleapis.com/css2?family=Montserrat:wght@300;400;500;600;700;800;900&display=swap" rel="stylesheet">
<style>
  :root {
    --green: #8cc63f;
    --red: #ed1b4b;
    --navy: #0f2c4c;
    --ink: #111111;
    --night: #120d1a;
    --ice: #eef5fb;
    --white: #ffffff;
    --sun: #fff38f;
  }
  * { box-sizing: border-box; margin: 0; padding: 0; }
  html, body { width: 716px; height: 1200px; overflow: hidden; background: var(--white); }
  body { font-family: "Montserrat", Arial, sans-serif; color: var(--ink); }
  .flyer { position: relative; width: 716px; height: 1200px; overflow: hidden; background: var(--white); }

  .hero-ring { position: absolute; left: 206px; top: 297px; width: 304px; height: 304px; border-radius: 50%; background: var(--red); }
  .hero-backdrop {
    position: absolute; left: 0; top: 0; width: 716px; height: 486px;
    background:
      radial-gradient(ellipse 240px 170px at 360px 230px, #c4445a 0%, #7a2a45 40%, rgba(40,20,50,0) 100%),
      radial-gradient(ellipse 260px 200px at 600px 420px, #173a66 0%, rgba(20,30,60,0) 100%),
      linear-gradient(180deg, #1a1524 0%, #151a2c 60%, #10213b 100%);
  }
  .headline-band { position: absolute; left: 0; top: 156px; width: 716px; height: 120px; background: rgba(8,6,12,0.72); }
  .headline { position: absolute; right: 157px; top: 172px; text-align: right; color: var(--white); line-height: 1; white-space: nowrap; }
  .headline .line-1 { font-size: 32px; font-weight: 300; display: block; }
  .headline .line-2 { font-size: 41px; font-weight: 300; display: block; margin-top: 4px; }
  .headline strong { font-weight: 800; }
  .headline .accent { color: var(--green); font-weight: 800; }

  .question-mark { position: absolute; left: 512px; top: 78px; font-size: 270px; font-weight: 900; color: var(--green); line-height: 1; }
  .thought-bubble { position: absolute; border-radius: 50%; background: var(--green); }
  .bubble-lg { left: 515px; top: 296px; width: 37px; height: 37px; }
  .bubble-sm { left: 471px; top: 327px; width: 24px; height: 24px; }

  .portrait { position: absolute; left: 220px; top: 311px; width: 276px; height: 276px; border-radius: 50%;
    background: radial-gradient(circle at 50% 55%, #fffbd0 0%, var(--sun) 70%, #f7e96a 100%); }

  .study-logo { position: absolute; left: 243px; top: -4px; width: 217px; height: 84px; background: var(--green);
    border: 2px solid var(--white); border-top: none; border-radius: 0 0 22px 22px; text-align: center; color: var(--navy); font-weight: 800; }
  .study-logo .name { display: block; font-size: 34px; letter-spacing: 4px; margin-top: 12px; line-height: 1; }
  .study-logo .sub { display: block; font-size: 14px; letter-spacing: 14px; margin-top: 8px; padding-left: 14px; line-height: 1; }

  .study-title { position: absolute; left: 0; top: 604px; width: 716px; text-align: center; font-size: 28px; font-weight: 500; line-height: 32px; }
  .study-title .accent { color: var(--red); }
  .study-title strong { font-weight: 800; }

  .about { position: absolute; left: 45px; top: 736px; width: 626px; height: 72px; border: 2px solid var(--navy); border-radius: 22px; background: var(--ice); }
  .about-tab { position: absolute; left: 64px; top: 725px; width: 240px; height: 21px; background: var(--green); border-radius: 12px 0 0 12px;
    color: var(--white); font-size: 15px; font-weight: 800; letter-spacing: 3px; line-height: 21px; padding-left: 13px; white-space: nowrap; overflow: hidden; }
  .about-icon { position: absolute; left: 295px; top: 713px; width: 45px; height: 45px; border-radius: 50%; background: var(--green); border: 2px solid var(--white); }
  .about-text { position: absolute; left: 45px; top: 760px; width: 626px; text-align: center; font-size: 15.5px; line-height: 20px; font-weight: 500; }
  .about-text strong { font-weight: 800; }

  .card-accent { position: absolute; border-radius: 12px; }
  .card { position: absolute; top: 846px; width: 283px; height: 155px; background: var(--white); border-radius: 10px; box-shadow: 2px 4px 8px rgba(0,0,0,0.35); }
  .card-icon { position: absolute; left: 8px; top: 7px; width: 46px; height: 46px; border-radius: 50%; }
  .card-title { position: absolute; left: 66px; font-weight: 600; white-space: nowrap; }
  .card-list { position: absolute; left: 26px; top: 60px; list-style: none; font-size: 11px; font-weight: 500; line-height: 13px; white-space: nowrap; }
  .card-list li { position: relative; padding-left: 18px; margin-bottom: 13px; }
  .card-list li::before { content: ""; position: absolute; left: 0; top: 2px; width: 9px; height: 9px; border-radius: 50%; }
  .card-involves .card-list li::before { background: var(--red); }
  .card-eligibility .card-list li::before { background: var(--green); }

  .compensation { position: absolute; left: 52px; top: 1044px; width: 612px; height: 44px; background: var(--red); border-radius: 6px;
    color: var(--white); font-size: 33px; font-weight: 900; letter-spacing: 1.5px; line-height: 44px; padding-left: 67px; white-space: nowrap; }
  .compensation svg { position: absolute; left: 14px; top: 5px; }

  .cta-pill { position: absolute; left: 83px; top: 1113px; width: 291px; height: 31px; border: 1.5px solid var(--ink); border-radius: 16px;
    font-size: 19.5px; font-weight: 800; line-height: 28px; text-align: center; white-space: nowrap; }
  .cta-more { position: absolute; left: 383px; top: 1113px; font-size: 19.5px; font-weight: 800; line-height: 30px; color: var(--red); white-space: nowrap; }

  .contact-bar { position: absolute; left: 0; top: 1160px; width: 716px; height: 40px; background: var(--navy); color: var(--white);
    text-align: center; font-size: 20px; font-weight: 500; letter-spacing: 1px; line-height: 40px; white-space: nowrap; }
  .contact-bar svg { vertical-align: -3px; margin-right: 8px; }
</style>
</head>
<body>
<main class="flyer">
  <div class="hero-ring"></div>
  <div class="hero-backdrop" role="img" aria-label="Glowing illustrated brain with light trails on a dark starry background"></div>
  <div class="headline-band"></div>
  <h1 class="headline">
    <span class="line-1">Is Your Child <strong>STRUGGLING</strong></span>
    <span class="line-2">with <span class="accent">OVERTHINKING</span></span>
  </h1>
  <div class="question-mark" aria-hidden="true">?</div>
  <div class="thought-bubble bubble-lg"></div>
  <div class="thought-bubble bubble-sm"></div>
  <div class="portrait" role="img" aria-label="Photo of a thoughtful child resting chin on hand, on a yellow background"></div>

  <div class="study-logo"><span class="name">MOLVT</span><span class="sub">STUDY</span></div>

  <h2 class="study-title">
    Join the <span class="accent">Marrowby Orchard</span><br>
    <span class="accent">Lantern Vesper Trail</span><br>
    <strong>(MOLVT)</strong> Studya
  </h2>

  <section>
    <div class="about"></div>
    <div class="about-tab">ABOUT THE STUDY</div>
    <div class="about-icon">
      <svg width="41" height="41" viewBox="0 0 41 41" fill="none" stroke="#fff" stroke-width="2" stroke-linejoin="round">
        <path d="M9 12 Q15 10 20 13 V30 Q15 27 9 29 Z"/>
        <path d="M32 12 Q26 10 21 13 V30 Q26 27 32 29 Z"/>
        <path d="M7 15 V31 Q14 29 20.5 32 Q27 29 34 31 V15"/>
      </svg>
    </div>
    <p class="about-text">University researchers are studying brain activity related to <strong>Emotions,</strong><br><strong>Decision-Making, Puberty, Anxiety,</strong> and <strong>Depression.</strong></p>
  </section>

  <div class="card-accent" style="left:38px;top:833px;width:105px;height:79px;background:var(--green)"></div>
  <div class="card-accent" style="left:92px;top:935px;width:253px;height:78px;background:var(--green)"></div>
  <div class="card card-involves" style="left:51px">
    <div class="card-icon" style="background:var(--red)">
      <svg width="46" height="46" viewBox="0 0 46 46" fill="#fff">
        <circle cx="15" cy="16" r="4"/><circle cx="31" cy="16" r="4"/><circle cx="23" cy="19" r="5"/>
        <path d="M8 31 Q8 22 15 22 Q19 22 20 24 L16 33 H8 Z"/>
        <path d="M38 31 Q38 22 31 22 Q27 22 26 24 L30 33 H38 Z"/>
        <path d="M14 35 Q14 25 23 25 Q32 25 32 35 Z"/>
      </svg>
    </div>
    <h3 class="card-title" style="top:23px;font-size:12.5px">What Participation Involves</h3>
    <ul class="card-list">
      <li>One 1-hour interview (online or in-person)</li>
      <li>Online questionnaires (parent &amp; child)</li>
      <li>One 2-hour visit including MRI scan,<br>puberty questions, and small hair sample</li>
    </ul>
  </div>

  <div class="card-accent" style="left:370px;top:833px;width:105px;height:79px;background:var(--red)"></div>
  <div class="card-accent" style="left:424px;top:935px;width:254px;height:78px;background:var(--red)"></div>
  <div class="card card-eligibility" style="left:383px">
    <div class="card-icon" style="background:var(--green)">
      <svg width="46" height="46" viewBox="0 0 46 46" fill="none" stroke="#fff" stroke-width="2">
        <circle cx="23" cy="19" r="10"/>
        <path d="M23 14 L24.5 17.5 L28 18 L25.3 20.3 L26 24 L23 22 L20 24 L20.7 20.3 L18 18 L21.5 17.5 Z" stroke-width="1.4"/>
        <path d="M16 27 L12 36 L16 35 L18 38 L21 30"/>
        <path d="M30 27 L34 36 L30 35 L28 38 L25 30"/>
      </svg>
    </div>
    <h3 class="card-title" style="top:19px;font-size:17.5px">Eligibility</h3>
    <ul class="card-list">
      <li>Girls age 10-17</li>
      <li>Who tend to worry or overthink negative</li>
      <li>No diagnosis of psychosis, learning<br>problems, or autism</li>
    </ul>
  </div>

  <div class="compensation">
    <svg width="38" height="36" viewBox="0 0 38 36" fill="#fff">
      <path d="M16 4 H24 L21 9 H19 Z"/>
      <path d="M19 9 Q30 12 30 22 Q30 28 20 28 Q11 28 11 22 Q11 12 19 9 Z"/>
      <text x="17" y="24" font-size="10" font-weight="700" fill="#ed1b4b" font-family="Montserrat, sans-serif">$</text>
      <path d="M2 26 H8 V35 H2 Z"/>
      <path d="M9 27 Q14 25 19 28 H26 Q28 29 26 31 H18 M9 33 H22 L34 27 Q36 26 35 29 L24 35 H9 Z"/>
    </svg>
    COMPENSATION UP TO $140
  </div>

  <div class="cta-pill">Interested In Participating?</div>
  <div class="cta-more">Want More Information?</div>

  <footer class="contact-bar">
    <svg width="18" height="13" viewBox="0 0 18 13" fill="none" stroke="#fff" stroke-width="1.6"><rect x="1" y="1" width="16" height="11"/><path d="M1 1 L9 7 L17 1 M1 12 L7 6 M17 12 L11 6"/></svg>molvtstudy@marrowby-lab.org
  </footer>
</main>
</body>
</html>
```